Harborline Coverage (02)

We're designing a website to sell Medicare Supplements. Attached is the content we want to say and general layout, but please use your best knowledge to make it better. This platform is intentionally simplistic because this is reaching an older demographic, so it should be very straightforward, attention-grabbing and extremely user-friendly, while still appearing reliable and professional.
This should be a two-page web design. The homepage has information on Medicare supplements (script in image attached below) along with a button to input zip code. This triggers a window to pop up asking for personal information (will also be listed in attachment).
This brings you to the second page that lists out the medicare supplement companies and plans based on inputed information. We just want to see the design you have in mind, so it doesn't matter what information you put in this section. Feel free to reference/replicate the information in image 3 in the doc. There should be a section where you can filter results by company, premium price, or coverage plans.
Target Market(s)
Seniors, 65+
Industry/Entity Type
Insurance
Number of Pages Required
2 page
Look and feel
Each slider illustrates characteristics of the customer's brand and the style your logo design should communicate.

```html
<!DOCTYPE html>
<html lang="en">
<head>
<meta charset="utf-8">
<title>Harborline Coverage — Get a Quote</title>
<link href="https://fonts.googleapis.com/css2?family=Bebas+Neue&family=Open+Sans:wght@400;600;700&display=swap" rel="stylesheet">
<style>
:root{
  --orange:#ef8a17;
  --orange-dark:#d97a0c;
  --ink:#3a3a3a;
  --text:#5a5a5a;
  --light:#f2f2f2;
  --sand:#f4ebe2;
  --night:#2a2a2a;
  --white:#ffffff;
  --veil:rgba(45,35,28,.55);
}
*{box-sizing:border-box;margin:0;padding:0}
html,body{width:743px;height:1200px;overflow:hidden}
body{position:relative;font-family:'Open Sans',sans-serif;color:var(--text);background:var(--white)}
.abs{position:absolute}
.display{font-family:'Bebas Neue',sans-serif;font-weight:400;letter-spacing:.2px}
.accent{color:var(--orange)}

/* hero */
.hero{left:0;top:0;width:743px;height:297px;background:var(--sand)}
.hero-photo{left:0;top:0;width:295px;height:297px;background:linear-gradient(135deg,#d9d2ca,#b9c6d0 60%,#9fb4c4);clip-path:polygon(0 0,100% 0,100% 100%,0 100%)}
.hero-brand{left:380px;top:20px;font-size:19px;color:var(--ink);line-height:1}
.hero-tag{left:381px;top:41px;width:170px;font-size:7px;line-height:10px;color:var(--text)}
.hero-price{left:470px;top:96px;font-size:26px;color:var(--orange);line-height:1}
.hero-btn{left:450px;top:210px;width:96px;height:29px;background:var(--ink);color:var(--white);font-size:11px;display:flex;align-items:center;justify-content:center}

/* benefits */
.benefits{left:0;top:297px;width:743px;height:344px;background:var(--light)}
.benefit-intro{left:0;width:743px;text-align:center;font-size:7px;color:var(--text)}
.benefit-photo{top:446px;width:95px;height:95px}
.benefit-dash{top:553px;width:15px;height:2px;background:var(--orange)}
.benefit-text{top:565px;width:96px;font-size:7px;line-height:10.4px}

/* costs */
.costs{left:0;top:641px;width:743px;height:371px;background:var(--sand)}
.costs-title{left:154px;top:677px;font-size:17px;line-height:16px;color:var(--ink)}
.costs-dash{left:154px;top:722px;width:19px;height:2px;background:var(--orange)}
.costs-copy{left:154px;top:735px;width:210px;font-size:6.9px;line-height:10.4px}
.costs-photo{left:381px;top:679px;width:207px;height:123px;background:var(--white);padding:3px;box-shadow:0 2px 6px rgba(0,0,0,.15)}
.costs-photo div{width:100%;height:100%;background:linear-gradient(120deg,#3d5a8a,#e9eef3 45%,#8fb7c4)}
.rate-card{top:824px;width:131px;height:150px;padding:11px 10px}
.rate-card .icon{width:33px;height:33px;background:rgba(255,255,255,.85);display:flex;align-items:center;justify-content:center}
.rate-card h3{font-size:10.5px;margin-top:16px;line-height:1}
.rate-card p{font-size:6.8px;line-height:9.7px;margin-top:8px}
.card-orange{left:154px;background:var(--orange);color:#fff3e0}
.card-orange h3{color:#fff8ee}
.card-dark{left:306px;background:#44474c;color:#e6e6e6}
.card-dark h3{color:var(--white)}
.card-light{left:457px;background:var(--white);color:var(--text)}
.card-light h3{color:var(--ink)}
.card-light .icon{background:#f1f1f1}

/* footer */
.footer{left:0;top:1012px;width:743px;height:188px;background:var(--night)}
.footer-brand{left:154px;top:1048px;font-size:18px;color:#e4e4e4;line-height:1}
.footer-copy{left:154px;width:240px;font-size:6.9px;line-height:10px;color:#bdbdbd}
.zip-title{left:421px;top:1048px;font-size:25px;color:#e8e8e8;line-height:1}
.zip-input{left:421px;top:1078px;width:78px;height:29px;background:#e9e9e9;display:flex;align-items:center;padding-left:8px;gap:9px;font-size:10px;color:var(--ink)}
.zip-btn{left:505px;top:1078px;width:84px;height:29px;background:var(--orange);color:var(--white);font-size:11.5px;display:flex;align-items:center;justify-content:center}
.footer-rule{left:154px;top:1159px;width:435px;height:1px;background:#555}
.legal{left:0;top:1174px;width:743px;text-align:center;font-size:5.6px;color:#9a9a9a}

/* veil + modal */
.veil{left:0;top:0;width:743px;height:1200px;background:var(--veil)}
.modal{left:220px;top:58px;width:304px;height:474px;background:var(--white)}
.close{left:283px;top:7px;width:13px;height:13px;border:1px solid var(--orange);font-size:8px;font-weight:700;color:var(--ink);display:flex;align-items:center;justify-content:center}
.modal-title{left:0;top:15px;width:304px;text-align:center;font-size:25px;color:var(--orange);line-height:1}
.modal-lead{left:26px;top:55px;width:256px;font-size:10.6px;line-height:13.4px;color:var(--ink)}
.modal-note{left:25px;top:94px;width:255px;font-size:7.2px;line-height:10.1px}
.required{left:25px;top:154px;font-size:7.3px;font-weight:600;color:var(--ink)}
.questions{left:25px;top:180px;font-size:10.5px;color:var(--ink)}
.label{font-size:7.3px;font-weight:600;color:var(--ink);left:25px}
.sublabel{font-size:5.8px;font-weight:700;color:var(--ink)}
.radio-row{left:25px;top:222px;display:flex;gap:14px;font-size:7.3px;align-items:center}
.radio{display:flex;align-items:center;gap:5px}
.radio i{width:9px;height:9px;border:1px solid var(--orange);border-radius:50%;display:flex;align-items:center;justify-content:center}
.radio i b{width:3px;height:3px;border-radius:50%;background:var(--ink)}
.field{width:119px;height:21px;border:1px solid var(--orange);border-radius:2px;font-size:7.3px;color:var(--text);display:flex;align-items:center;justify-content:space-between;padding:0 8px}
.btn{top:427px;height:22px;font-size:9px;color:var(--white);display:flex;align-items:center;justify-content:center;border-radius:2px}
.btn-primary{left:25px;width:101px;background:var(--orange)}
.btn-cancel{left:134px;width:38px;background:#1e1e1e}
</style>
</head>
<body>

<section class="abs hero">
  <div class="abs hero-photo" role="img" aria-label="Photo of active seniors stretching in a bright room"></div>
  <div class="abs display hero-brand"><span class="accent">Harborline</span> Coverage</div>
  <p class="abs hero-tag">Be confident choosing the Medicare Supplement plan that's right for you.</p>
  <div class="abs display hero-price">From $103</div>
  <div class="abs display hero-btn">Get Free Quotes</div>
</section>

<section class="abs benefits">
  <p class="abs benefit-intro" style="top:89px">Each Medicare Supplement plan covers the same basic benefits, and every plan will include</p>
  <p class="abs benefit-intro" style="top:110px">Medicare Supplement plans vary in coverage, but all plans</p>
</section>
<div class="abs benefit-photo" style="left:154px;background:linear-gradient(135deg,#5a3d2a,#c79a6e)" role="img" aria-label="Photo of a man drinking tea"></div>
<div class="abs benefit-photo" style="left:267px;background:linear-gradient(135deg,#6b7c8a,#c9d2d8)" role="img" aria-label="Photo of hospice care"></div>
<div class="abs benefit-photo" style="left:381px;background:linear-gradient(135deg,#d9d9d9,#f3eee8)" role="img" aria-label="Photo of a doctor's visit"></div>
<div class="abs benefit-photo" style="left:494px;background:linear-gradient(135deg,#eef0f4,#2d3f8c)" role="img" aria-label="Photo of a gloved hand holding a blood sample"></div>
<div class="abs benefit-dash" style="left:154px"></div>
<div class="abs benefit-dash" style="left:267px"></div>
<div class="abs benefit-dash" style="left:381px"></div>
<div class="abs benefit-dash" style="left:494px"></div>
<p class="abs benefit-text" style="left:154px">Medicare Part A coinsurance costs up to an additional 365 days after Medicare benefits are exhausted</p>
<p class="abs benefit-text" style="left:267px">Medicare Part A hospice care coinsurance or copayments</p>
<p class="abs benefit-text" style="left:381px">Medicare Part B coinsurance or copayments</p>
<p class="abs benefit-text" style="left:494px">First three pints of blood used in a medical procedure</p>

<section class="abs costs"></section>
<h2 class="abs display costs-title"><span class="accent">Medicare Supplement</span><br>Insurance Plan Costs</h2>
<div class="abs costs-dash"></div>
<p class="abs costs-copy">Although private insurance companies are required to offer the same basic benefits for each lettered plan, they do have the ability to charge different premiums. You might want to shop around to find a Medicare Supplement insurance plan that may fit your medical and financial needs. Insurance companies may price their plan premiums in any of the following ways:</p>
<div class="abs costs-photo"><div role="img" aria-label="Photo of a nurse talking with a senior patient"></div></div>

<article class="abs rate-card card-orange">
  <div class="icon"><svg width="20" height="20" viewBox="0 0 20 20" fill="none" stroke="#555" stroke-width="1.3"><path d="M3 9h14c0 4-3 6-7 6s-7-2-7-6z"/><path d="M7 15l-1 3h8l-1-3"/><path d="M10 10.5v3M8.5 12h3"/><path d="M12 8l4-5"/></svg></div>
  <h3 class="display">Community No-Age-Rated</h3>
  <p>These Medicare Supplement insurance plans charge premiums that are the same across the board, regardless of age.</p>
</article>
<article class="abs rate-card card-dark">
  <div class="icon"><svg width="20" height="20" viewBox="0 0 20 20" fill="none" stroke="#555" stroke-width="1.3"><circle cx="10" cy="7" r="4"/><path d="M3 18c0-4 3-6 7-6s7 2 7 6"/></svg></div>
  <h3 class="display">Issue-Age-Rated</h3>
  <p>These plans base their premiums on your age when you first enrolled in the policy. Therefore, the younger you are when you enroll in this type of plan, the lower your premium will be.</p>
</article>
<article class="abs rate-card card-light">
  <div class="icon"><svg width="22" height="22" viewBox="0 0 22 22" fill="none" stroke="#444" stroke-width="1.5"><circle cx="9" cy="9" r="6"/><path d="M9 6v6M6 9h6M13.5 13.5l5 5"/></svg></div>
  <h3 class="display">Attained-Age-Rated</h3>
  <p>Like issue-age-rated, these plans base their premiums on the age you were when you first bought a policy, but unlike issue-age-rated, premiums increase as you get older.</p>
</article>

<footer class="abs footer"></footer>
<div class="abs display footer-brand"><span class="accent">Harborline</span> Coverage</div>
<p class="abs footer-copy" style="top:1071px">Be confident choosing the Medicare Supplement plan that's right for you.</p>
<p class="abs footer-copy" style="top:1090px">We know insurance can be confusing. With so much information and not enough answers, we're here to help you find the plan that works best for you, your family and your health.</p>
<div class="abs display zip-title">Enter Zip Code.</div>
<div class="abs zip-input"><svg width="13" height="15" viewBox="0 0 13 15" fill="none" stroke="#ef8a17" stroke-width="1.2"><path d="M6.5 14s5-4.5 5-8.5a5 5 0 0 0-10 0c0 4 5 8.5 5 8.5z"/><circle cx="6.5" cy="5.5" r="1.8"/></svg>12311</div>
<div class="abs display zip-btn">Get Free Quotes</div>
<div class="abs footer-rule"></div>
<p class="abs legal">Copyright ©2020 Harborline Coverage. All rights reserved. &nbsp;I&nbsp; Terms &amp; Privacy Policy</p>

<div class="abs veil"></div>

<div class="abs modal" role="dialog" aria-label="Get a quote">
  <div class="abs close">X</div>
  <h1 class="abs display modal-title">Get A Quote</h1>
  <p class="abs display modal-lead">To figure out what your monthly premium would be, enter your gender and date of birth</p>
  <p class="abs modal-note">Individuals who attain the age of 65 on or after January 1, 2020, or who first become eligible for Medicare benefits due to age, disability, or end-stage renal disease on or after January 1, 2020, can't purchase a Medicare Supplement plan that covers the Part B deductible such as Plans C, F or High Deductible F.</p>
  <p class="abs required"><span class="accent">*</span> Required Gender</p>
  <h2 class="abs display questions">Questions Include:</h2>

  <p class="abs label" style="top:206px">Gender<span class="accent">*</span></p>
  <div class="abs radio-row">
    <span class="radio"><i><b></b></i>Male</span>
    <span class="radio"><i></i>Female</span>
  </div>

  <p class="abs label" style="top:246px">Date of Birth<span class="accent">*</span></p>
  <div class="abs field" style="left:25px;top:263px">mm/dd/yyyy</div>

  <p class="abs label" style="top:298px">Hospital Insurnace (Part A)<span class="accent">*</span></p>
  <p class="abs sublabel" style="left:25px;top:314px">Part A Month</p>
  <p class="abs sublabel" style="left:151px;top:314px">Part A Year</p>
  <div class="abs field" style="left:25px;top:329px">Year<svg width="7" height="5" viewBox="0 0 7 5"><path d="M1 1l2.5 2.5L6 1" fill="none" stroke="#ef8a17" stroke-width="1"/></svg></div>
  <div class="abs field" style="left:151px;top:329px">Year<svg width="7" height="5" viewBox="0 0 7 5"><path d="M1 1l2.5 2.5L6 1" fill="none" stroke="#ef8a17" stroke-width="1"/></svg></div>

  <p class="abs label" style="top:363px">Medical Insurance (Part B)<span class="accent">*</span></p>
  <p class="abs sublabel" style="left:25px;top:379px">Part B Month</p>
  <p class="abs sublabel" style="left:151px;top:379px">Part B Year</p>
  <div class="abs field" style="left:25px;top:394px">Year<svg width="7" height="5" viewBox="0 0 7 5"><path d="M1 1l2.5 2.5L6 1" fill="none" stroke="#ef8a17" stroke-width="1"/></svg></div>
  <div class="abs field" style="left:151px;top:394px">Year<svg width="7" height="5" viewBox="0 0 7 5"><path d="M1 1l2.5 2.5L6 1" fill="none" stroke="#ef8a17" stroke-width="1"/></svg></div>

  <div class="abs display btn btn-primary">Desired Coverage Start Date</div>
  <div class="abs display btn btn-cancel">Cancel</div>
</div>

</body>
</html>
```